InnRiderz Web Temp | ||
Web Temp | ||
Transportation | ||
www.innriderz.example | ||
Inn Riderz provides transportation from the top hotels around the world to the airports and vice versa. | ||
I would like to see a clean website, which looks very professional and inspires confidence in the user that the service is outstanding. It needs to look good with our logo, which has been uploaded for your reference. I would like the designer to include the text at the bottom of the pdf file that was uploaded. Additionally, there should be an area on the site that states, "Book Hotels, Flights...." followed by a buttom and "powered by trovask" |
Professional Sophisticated Corporate Modern Elegant |
below header | ||
trovask.example | ||
global-gate-shuttle.example | ||
pelunta.example | ||
Similar to trovask and pelunta, the site needs to be engaging. Most importantly it needs to show the following drop down input fields. (1) Select a country (2) Select a city (3) Rountrip (followed by circle that users can select) (4) One Way (followed by circle that users can select) (5) Select Hotel (drop down menu) (6) Select airport (drop down menu) (7) Arriving/Departing (pop up calendar). I have uploaded another file with a very crude mock up. But the text at the bottom of that sample should be included. I would like the designer to include the text at the bottom of the pdf file that was uploaded. Additionally, there should be an area on the site that states, "Book Hotels, Flights...." followed by a buttom and "powered by trovask" |

```html
<!DOCTYPE html>
<html lang="en">
<head>
<meta charset="utf-8">
<title>Inn Riderz – Hotel to Airport Transfers</title>
<link href="https://fonts.googleapis.com/css2?family=Arimo:ital,wght@0,400;0,700;1,400;1,700&family=Kalam:wght@400&display=swap" rel="stylesheet">
<style>
:root{
  --page-grey:#6b6b6b;
  --bar-dark:#4a4a4a;
  --white:#ffffff;
  --navy:#15386e;
  --navy-light:#2a5aa0;
  --sky:#2f9ad6;
  --sky-dark:#1f78b8;
  --nav-active:#5b4632;
  --cream:#f7edd5;
  --cream-edge:#e6d3a8;
  --orange:#e8741c;
  --ink:#2b2b2b;
  --muted:#6e6e6e;
  --field:#f4f7fb;
  --footer:#9a9a9a;
}
*{box-sizing:border-box;margin:0;padding:0}
html,body{width:1200px;height:901px;overflow:hidden;background:var(--page-grey);font-family:"Arimo",Arial,sans-serif;color:var(--ink)}
.canvas{position:relative;width:1200px;height:901px;overflow:hidden;background:var(--page-grey)}
.abs{position:absolute}

.top-bar{left:0;top:0;width:1200px;height:54px;background:var(--bar-dark);display:flex;justify-content:flex-end;align-items:center;gap:0;padding-right:150px}
.top-bar a{color:var(--white);text-decoration:none;font-size:15px;font-weight:700;padding:0 22px;border-left:1px solid #777}
.top-bar a:first-child{border-left:none;font-weight:400}

.sheet{left:158px;top:54px;width:884px;height:786px;background:var(--white)}

.brand{left:230px;top:70px;display:flex;align-items:center;gap:14px}
.brand-dot{width:62px;height:62px;border-radius:50%;background:var(--navy)}
.brand-name{font-size:40px;font-weight:700;color:var(--navy);letter-spacing:.5px}
.brand-line{left:306px;top:122px;font-size:9px;color:var(--muted);letter-spacing:.6px;text-transform:uppercase}

.tagline{left:680px;top:62px;width:300px;font-family:"Kalam",cursive;font-size:17px;line-height:20px;color:var(--orange);font-style:italic}
.call{left:760px;top:174px;font-size:13px;font-weight:700;color:var(--navy)}

.main-nav{left:224px;top:195px;width:769px;height:46px;background:linear-gradient(var(--navy-light),var(--navy));display:flex;align-items:center}
.main-nav a{color:var(--white);text-decoration:none;font-size:18px;font-weight:700;height:46px;line-height:46px;padding:0 30px}
.main-nav a.active{background:var(--nav-active)}

.hero{left:224px;top:241px;width:769px;height:178px;background:linear-gradient(#6fb7e6 0%,#b6dcef 30%,#d9b58f 48%,#c98a5e 58%,#3fb7c8 72%,#1b9fb8 100%)}
.hero-caption{left:470px;top:322px;width:523px;height:42px;background:linear-gradient(90deg,rgba(31,120,184,.85),rgba(31,120,184,.55));border-radius:22px 0 0 22px;color:var(--white);font-size:21px;font-weight:700;font-style:italic;line-height:42px;padding-left:32px}

.booking{left:224px;top:421px;width:238px;height:377px;border:3px solid var(--sky);background:var(--white)}
.booking-title{position:absolute;left:-3px;top:-3px;width:238px;height:36px;background:linear-gradient(var(--sky),var(--sky-dark));color:var(--white);font-size:19px;font-weight:700;text-align:center;line-height:36px;border-radius:8px 8px 0 0}
.booking-body{position:absolute;left:10px;top:40px;width:210px;font-size:10px;color:var(--ink)}
.select{height:17px;border:1px solid #9ab;background:var(--field);font-size:9px;font-weight:700;padding:2px 4px;margin-bottom:4px;width:110px;position:relative}
.select::after{content:"";position:absolute;right:4px;top:6px;border:4px solid transparent;border-top-color:#345}
.row{display:flex;align-items:center;gap:5px;margin-bottom:4px;font-size:9px;font-weight:700}
.radio{width:9px;height:9px;border:1px solid #567;border-radius:50%;background:var(--white)}
.check{width:9px;height:9px;border:1px solid #567;background:var(--white)}
.input{height:13px;border:1px solid #9ab;background:var(--white)}
.booking-foot{position:absolute;left:-3px;bottom:-3px;width:238px;height:22px;background:var(--sky-dark);color:var(--white);font-size:11px;font-style:italic;font-weight:700;line-height:22px;padding-left:10px}

.welcome{left:477px;top:428px;width:516px;height:168px;background:var(--cream);border:1px solid var(--cream-edge);border-radius:0 0 0 28px;padding:12px 20px}
.welcome h2{font-size:24px;color:var(--sky-dark);margin-bottom:6px}
.welcome p{font-size:15px;line-height:19px;color:var(--navy)}

.why{left:477px;top:606px;width:314px;height:192px;background:var(--cream);border:1px solid var(--cream-edge)}
.box-head{height:34px;background:linear-gradient(var(--sky),var(--sky-dark));color:var(--white);font-size:19px;font-weight:700;line-height:34px;text-align:center}
.why ul{list-style:none;padding:10px 16px}
.why li{display:flex;align-items:center;gap:10px;font-size:15px;font-weight:700;font-style:italic;color:var(--orange);margin-bottom:9px}
.more{position:absolute;left:20px;bottom:10px;background:var(--navy);color:var(--white);font-size:10px;font-weight:700;padding:3px 10px;border-radius:3px}

.gallery{left:798px;top:606px;width:195px;height:192px;background:var(--cream);border:1px solid var(--cream-edge)}
.thumbs{display:grid;grid-template-columns:1fr 1fr;gap:6px 10px;padding:8px 14px}
.thumb{text-align:center;font-size:8px;font-weight:700;color:var(--navy)}
.thumb-img{height:42px;margin-bottom:2px}
.gallery .more{left:auto;right:14px}

.global{left:224px;top:802px;width:769px;height:30px;display:flex;align-items:center;gap:5px}
.global strong{font-size:17px;color:var(--ink);margin-right:10px}
.flag{width:16px;height:10px}
.social{margin-left:auto;display:flex;gap:5px}
.social span{width:14px;height:14px;border-radius:50%;background:#8a96a8}

.footer{left:0;top:840px;width:1200px;height:61px;background:var(--footer)}
.footer-links{left:0;top:848px;width:1200px;display:flex;justify-content:center;gap:0;font-size:14px;color:var(--white)}
.footer-links span{padding:0 14px;border-left:1px solid var(--white)}
.footer-links span:first-child{border-left:none}
.copy{left:0;top:882px;width:1200px;text-align:center;font-size:10px;color:var(--white)}
</style>
</head>
<body>
<div class="canvas">
  <nav class="abs top-bar">
    <a>Already a member?</a><a>Sign In</a><a>My Account</a><a>Customer Support</a><a>Feedback</a>
  </nav>

  <div class="abs sheet"></div>

  <div class="abs brand"><span class="brand-dot"></span><span class="brand-name">Inn Riderz</span></div>
  <div class="abs brand-line">Hotel to airport transfers worldwide</div>
  <p class="abs tagline">Inn Riderz provides transportation from the top hotels around the world.</p>
  <p class="abs call">Call our travel experts: 1800 555 0199</p>

  <nav class="abs main-nav">
    <a class="active">Home</a><a>Flights</a><a>Holiday Packages</a><a>Activities</a><a>Weekend Gatawys</a>
  </nav>

  <div class="abs hero" role="img" aria-label="Beachfront resort with pool, palm trees and guests relaxing in the water"></div>
  <div class="abs hero-caption">Explore this Wonder of the World from the air....</div>

  <section class="abs booking">
    <div class="booking-title">BOOK YOUR TRAVEL</div>
    <div class="booking-body">
      <div class="select">Select a country</div>
      <div class="select" style="width:80px">Select a city</div>
      <div class="row"><span class="radio"></span>Arrival <span class="radio"></span>Departure</div>
      <div class="row"><span class="input" style="width:50px"></span>Arrival Date</div>
      <div class="row"><span class="input" style="width:50px"></span>Arrival Time</div>
      <div class="row"><span class="check"></span>Search Specific Dates:</div>
      <div class="row"><span class="select" style="width:40px;margin:0">Feb</span><span class="select" style="width:30px;margin:0"></span></div>
      <div class="row"><span class="select" style="width:40px;margin:0">Feb</span><span class="select" style="width:30px;margin:0"></span></div>
      <div class="row"><span class="radio"></span>Airport <span class="radio"></span>Airline</div>
      <div class="row"><span class="input" style="width:50px"></span>Flight Number</div>
      <div class="row"><span class="input" style="width:50px"></span>Vehicle Type</div>
      <div class="row"><span class="radio"></span>Hotel <span style="margin-left:14px">Check-in</span><span>Check-out</span><span>Rooms</span></div>
      <div class="row"><span class="radio"></span>Flight <span class="input" style="width:38px;margin-left:10px"></span><span class="input" style="width:38px"></span><span class="input" style="width:20px"></span></div>
      <div class="row"><span class="radio"></span>Car <span style="margin-left:30px">Adults</span><span>Kids</span></div>
      <div class="row"><span class="radio"></span>Activities <span class="input" style="width:22px"></span><span class="input" style="width:22px"></span></div>
      <div class="row" style="margin-top:6px">Hotel</div>
      <div style="font-size:8px;color:var(--muted);margin-bottom:3px">Find a hotel near a city, landmark, or airport</div>
      <div class="input" style="width:200px"></div>
    </div>
    <div class="booking-foot">Inn Riderz Booking</div>
  </section>

  <section class="abs welcome">
    <h2>Welcome,</h2>
    <p>Experience comfort and style Inn Riderz. Inn Riderz is surrounded by the energy of Union Square and is an ideal hotel destination to return to after exploring the renowned sights and attractions of the "City by the Bay." Inn Riderz will discover comfortable accommodations, friendly services, all offered at affordable rates.</p>
  </section>

  <section class="abs why">
    <div class="box-head">Why Inn Riderz?</div>
    <ul>
      <li><svg width="18" height="16" viewBox="0 0 18 16"><path d="M2 8 L7 13 L16 2" fill="none" stroke="#1f78b8" stroke-width="3"/></svg>Customer care available 24/7</li>
      <li><svg width="18" height="16" viewBox="0 0 18 16"><path d="M2 8 L7 13 L16 2" fill="none" stroke="#1f78b8" stroke-width="3"/></svg>Hand-picked tours &amp; experiences</li>
      <li><svg width="18" height="16" viewBox="0 0 18 16"><path d="M2 8 L7 13 L16 2" fill="none" stroke="#1f78b8" stroke-width="3"/></svg>No fee to change your dates</li>
      <li><svg width="18" height="16" viewBox="0 0 18 16"><path d="M2 8 L7 13 L16 2" fill="none" stroke="#1f78b8" stroke-width="3"/></svg>Lowest prices - guaranteed</li>
    </ul>
    <span class="more">More</span>
  </section>

  <section class="abs gallery">
    <div class="box-head">Gallery</div>
    <div class="thumbs">
      <div class="thumb"><div class="thumb-img" role="img" aria-label="Mountain palace" style="background:linear-gradient(#7fb3dc,#b88a5a)"></div>Potala</div>
      <div class="thumb"><div class="thumb-img" role="img" aria-label="Rafting on a river" style="background:linear-gradient(#5d8fb8,#d9e6ee)"></div>whitewater rafting</div>
      <div class="thumb"><div class="thumb-img" role="img" aria-label="Snowy ski slope" style="background:linear-gradient(#9cc6e6,#eef3f7)"></div>Ski</div>
      <div class="thumb"><div class="thumb-img" role="img" aria-label="Coastal lagoon" style="background:linear-gradient(#4aa2d4,#2f6f9a)"></div>island cruise</div>
    </div>
    <span class="more">More</span>
  </section>

  <div class="abs global">
    <strong>Global Sites:</strong>
    <span class="flag" style="background:#c8102e"></span>
    <span class="flag" style="background:#1e4fa0"></span>
    <span class="flag" style="background:#f2c200"></span>
    <span class="flag" style="background:#009246"></span>
    <span class="flag" style="background:#d52b1e"></span>
    <span class="flag" style="background:#ffffff;border:1px solid #bbb"></span>
    <span class="flag" style="background:#0055a4"></span>
    <span class="flag" style="background:#ff9933"></span>
    <span class="flag" style="background:#006b3f"></span>
    <span class="flag" style="background:#ce1126"></span>
    <span class="flag" style="background:#003893"></span>
    <span class="flag" style="background:#fecb00"></span>
    <span class="flag" style="background:#00247d"></span>
    <div class="social"><span></span><span></span><span></span></div>
  </div>

  <div class="abs footer"></div>
  <div class="abs footer-links"><span>Best Price Guarantee</span><span>About Us</span><span>Press Centre</span><span>Travel News</span></div>
  <p class="abs copy">© 2012. Inn Riderz</p>
</div>
</body>
</html>
```